当社は現在「venrola」という通販サイトを運用しておりますが、その通販サイトを海苔専門のサイトにリニューアル予定となっております。
海苔をメインとしたサイトにリニューアルするに伴い、ラベルデザインを一新したいと考えております。
海苔と言っても、「全形海苔」「刻み海苔」「海苔ふりかけ」など様々な商品を掲載予定です。
まずは1つの共通ラベルデザインで全商品を販売していきたいと思っております。
有明海の「海」と「海苔」がモチーフになっているような、昔のように見えて新しいデザインを希望致します。
・シック
・シンプル
・色は少なめ
・オレンジor茶系or黒系

透明のジッパー付きチャック袋にラベルを張る予定となっております。
袋サイズ:約240×360
ラベルサイズ:約100×100
添付画像のような書体及びシンプルなデザインを希望します
度々の追記、申し訳ございません。
可能な方だけで構いませんので、当社ロゴもデザインの中に入れて頂けますと幸いです。
どうぞ宜しくお願い致します。

海苔という日本の伝統食に斬新なアレンジを付加して頂いたデザインを選ばせて頂きました。

この度は素晴らしいご提案の数々をありがとうございました。
今後ともどうぞ宜しくお願い致します。

```html
<!DOCTYPE html>
<html lang="ja">
<head>
<meta charset="UTF-8">
<title>潮凪海苔 ラベル</title>
<link href="https://fonts.googleapis.com/css2?family=Shippori+Mincho:wght@500&display=swap" rel="stylesheet">
<style>
  :root {
    --canvas-bg: #ecebe8;
    --label-peach: #f3cfc2;
    --label-peach-soft: #f7e2da;
    --label-white: #fdf9f7;
    --ink: #1b1b1b;
    --accent-red: #c9322b;
  }
  * { margin: 0; padding: 0; box-sizing: border-box; }
  html, body {
    width: 706px;
    height: 1200px;
    overflow: hidden;
    background: var(--canvas-bg);
  }
  .canvas {
    position: relative;
    width: 706px;
    height: 1200px;
    display: flex;
    align-items: center;
    justify-content: center;
  }
  .label {
    position: relative;
    width: 540px;
    height: 640px;
    background: linear-gradient(180deg,
      var(--label-peach) 0%,
      var(--label-peach) 55%,
      var(--label-peach-soft) 82%,
      var(--label-white) 100%);
    box-shadow: 0 2px 6px rgba(0,0,0,0.08);
  }
  .product-name {
    position: absolute;
    top: 70px;
    left: 50%;
    transform: translateX(-50%);
    writing-mode: vertical-rl;
    font-family: "Shippori Mincho", serif;
    font-weight: 500;
    font-size: 82px;
    line-height: 1;
    letter-spacing: 0.32em;
    color: var(--ink);
  }
  .brand-line {
    position: absolute;
    left: 50%;
    bottom: 58px;
    transform: translateX(-50%);
    display: flex;
    flex-direction: column;
    align-items: center;
    gap: 12px;
  }
  .brand-square {
    width: 22px;
    height: 22px;
    background: var(--accent-red);
  }
  .brand-text {
    font-family: "Shippori Mincho", serif;
    font-weight: 500;
    font-size: 15px;
    letter-spacing: 0.28em;
    color: var(--ink);
    white-space: nowrap;
  }
</style>
</head>
<body>
  <main class="canvas">
    <section class="label">
      <h1 class="product-name">潮凪海苔</h1>
      <div class="brand-line">
        <div class="brand-square"></div>
        <p class="brand-text">SHIONAGI SEAWEED</p>
      </div>
    </section>
  </main>
</body>
</html>
```